Careerfold Background Picture

Job Title:
Professional Careerfold Banner Design for Individual in Architectural Industry

Description:

Hello talented designers,

I am looking for a creative and professional graphic designer to create a Careerfold banner for my personal profile. I am deeply involved in the architectural systems industry, specializing in innovative and sustainable building solutions.

What I'm Looking For:

Personal Branding: The banner should reflect my professional identity and role in the architectural systems industry. It should be more personal than corporate.

Visual Elements: Include imagery or abstract designs that represent architecture, innovation, and sustainability. The design should subtly hint at my industry expertise and areas of specialization.

Professional and Engaging: The design should be visually striking but maintain a professional look. It should engage viewers and encourage them to learn more about my professional background and skills.

File Requirements: The final design should be provided in a high-resolution JPEG or PNG format, fitting Careerfold's banner dimensions.

To Apply, Please Provide:

A summary of your design experience, especially with Careerfold banners or personal branding projects.
A portfolio showcasing your previous work, highlighting any designs related to personal branding or professional themes.
Your estimated timeline and budget for the project.
Selection Criteria:

Creativity in reflecting a personal professional brand.
Experience with individual professional branding.
Quality and relevance of the portfolio.
Competitive pricing and clear communication.
I am excited to see your creative approaches and look forward to collaborating to craft a banner that perfectly encapsulates my professional persona on Careerfold.

Thank you!

My careerfold page:
careerfold.net/in/morvendique

Our website:

https://filevault-example.net/share/folders/7qTxP2mWk9RbZs4LhYdNc03vAefJo?ref=share_link

Some photos of our projects:

```html
<!DOCTYPE html>
<html lang="en">
<head>
<meta charset="utf-8">
<title>Careerfold Banner – Architecture, Innovation &amp; Sustainability</title>
<link rel="stylesheet" href="https://fonts.googleapis.com/css2?family=Oswald:wght@400;500&display=swap">
<style>
  :root {
    --page-bg: #f3f4f6;
    --navy: #1b3f8c;
    --sky-blue: #74a8ea;
    --arc-grey: #b8c5d9;
    --banner-light: #f5f7fb;
    --banner-mid: #e6ebf3;
    --white: #ffffff;
  }
  html, body {
    margin: 0;
    width: 1200px;
    height: 1200px;
    overflow: hidden;
    background: var(--page-bg);
  }
  .canvas {
    position: relative;
    width: 1200px;
    height: 1200px;
  }
  .profile-banner {
    position: absolute;
    left: 50px;
    top: 462px;
    width: 1100px;
    height: 275px;
    display: block;
  }
  .banner-heading {
    font-family: 'Oswald', 'Arial Narrow', sans-serif;
    font-weight: 500;
    font-size: 23px;
    fill: var(--white);
  }
</style>
</head>
<body>
<main class="canvas">
  <svg class="profile-banner" viewBox="0 0 792 198" xmlns="http://www.w3.org/2000/svg">
    <defs>
      <linearGradient id="facade-wash" x1="0" y1="0" x2="1" y2="0">
        <stop offset="0" stop-color="var(--banner-light)"/>
        <stop offset="0.5" stop-color="var(--banner-mid)"/>
        <stop offset="1" stop-color="var(--banner-light)"/>
      </linearGradient>
      <linearGradient id="interior-tone" x1="0" y1="0" x2="0" y2="1">
        <stop offset="0" stop-color="#d9dde2"/>
        <stop offset="0.6" stop-color="#c9ccd0"/>
        <stop offset="1" stop-color="#a88f72"/>
      </linearGradient>
      <linearGradient id="tower-tone" x1="0" y1="0" x2="0" y2="1">
        <stop offset="0" stop-color="#7fb2ee"/>
        <stop offset="0.5" stop-color="#3d5f93"/>
        <stop offset="1" stop-color="#1f2c45"/>
      </linearGradient>
      <clipPath id="banner-clip"><rect width="792" height="198"/></clipPath>
      <filter id="photo-shadow" x="-10%" y="-10%" width="130%" height="130%">
        <feDropShadow dx="2" dy="3" stdDeviation="3" flood-opacity="0.3"/>
      </filter>
    </defs>

    <g clip-path="url(#banner-clip)">
      <rect class="banner-backdrop" width="792" height="198" fill="url(#facade-wash)" role="img" aria-label="Faded photo of a modern apartment facade"/>

      <g class="arc-rings" fill="none" stroke="var(--arc-grey)" stroke-width="2.5">
        <circle cx="-44" cy="60" r="100"/>
        <circle cx="-44" cy="60" r="128"/>
        <circle cx="-44" cy="60" r="156"/>
        <circle cx="-44" cy="60" r="184"/>
        <circle cx="-44" cy="60" r="212"/>
        <circle cx="-44" cy="60" r="240"/>
      </g>

      <rect class="accent-bar-left" x="0" y="137" width="131" height="31" fill="var(--sky-blue)"/>

      <g class="dot-column" fill="var(--navy)">
        <circle cx="133" cy="51" r="1.8"/><circle cx="133" cy="63" r="1.8"/>
        <circle cx="133" cy="75" r="1.8"/><circle cx="133" cy="87" r="1.8"/>
        <circle cx="252" cy="83" r="1.8"/><circle cx="252" cy="94" r="1.8"/>
        <circle cx="252" cy="105" r="1.8"/><circle cx="252" cy="116" r="1.8"/>
        <circle cx="463" cy="2" r="1.8"/><circle cx="463" cy="13" r="1.8"/>
      </g>

      <rect class="accent-bar-navy" x="268" y="80" width="68" height="27" fill="var(--navy)"/>
      <rect class="accent-bar-sky" x="315" y="18" width="164" height="42" fill="var(--sky-blue)"/>

      <rect class="project-photo" x="220" y="0" width="95" height="80" fill="url(#interior-tone)" role="img" aria-label="Bright apartment interior with large windows"/>
      <rect class="project-photo" x="292" y="18" width="122" height="135" fill="url(#tower-tone)" role="img" aria-label="Modern mid-rise residential building against blue sky"/>
      <rect class="project-photo" x="414" y="60" width="163" height="121" fill="url(#interior-tone)" filter="url(#photo-shadow)" role="img" aria-label="Empty living room with corner windows and wood floor"/>

      <rect class="accent-square" x="547" y="132" width="60" height="60" fill="var(--sky-blue)" opacity="0.85"/>

      <g class="heading-bars">
        <rect x="607" y="32" width="185" height="31" fill="var(--navy)"/>
        <rect x="607" y="83" width="185" height="32" fill="var(--navy)"/>
        <rect x="607" y="136" width="185" height="32" fill="var(--navy)"/>
        <text class="banner-heading" x="699.5" y="56" text-anchor="middle">Architecture</text>
        <text class="banner-heading" x="699.5" y="107.5" text-anchor="middle">Innovation &amp;</text>
        <text class="banner-heading" x="699.5" y="160.5" text-anchor="middle">Sustainability</text>
      </g>
    </g>
  </svg>
</main>
</body>
</html>
```